Web Design Project

We need a web site design for a new company based in New York/New Jersey called "The Lumenfold Group". We develop innovative strategies for marketing, strategic planning, business development, public relations in economic development. Simply put we create innovative strategies for invigorating smarter and stronger leaders and companies. We are a consulting firm with bold ideas for affecting change. We want to communicate that partnering with The Lumenfold Group your first decision to breakthrough innovation.

Target Market(s)

The target audience for the consulting services are private companies, economic development organizations, government and other interested in community investment strategies globally.

Industry/Entity Type

Business

Font styles to use
Serif
Sans Serif

Requirements
Must have
Nice to have
Should not have

```html
<!DOCTYPE html>
<html lang="en">
<head>
<meta charset="utf-8">
<title>The Lumenfold Group</title>
<link href="https://fonts.googleapis.com/css2?family=Open+Sans:wght@300;400;600;700&display=swap" rel="stylesheet">
<style>
:root{
  --red:#b8262c;
  --navy:#1f2f4f;
  --blue:#1a78c8;
  --blue-dark:#105a9e;
  --ink:#333;
  --muted:#888;
  --light:#ececec;
  --paper:#fff;
  --dark:#1b1b1b;
  --dark2:#262626;
}
*{box-sizing:border-box;margin:0;padding:0}
html,body{width:1200px;height:2356px;overflow:hidden}
body{font-family:"Open Sans",Arial,sans-serif;color:var(--ink);background:var(--light);position:relative}
.abs{position:absolute}

/* header */
.site-header{left:0;top:0;width:1200px;height:88px;background:var(--paper);box-shadow:0 2px 6px rgba(0,0,0,.15)}
.brand{left:236px;top:26px;font-weight:700;font-size:26px;color:var(--navy);line-height:1}
.contact-tab{left:716px;top:0;width:404px;height:32px;background:var(--red);color:#fff;font-size:12px;display:flex;align-items:center;justify-content:center;gap:28px;border-radius:0 0 6px 6px}
.main-nav{left:752px;top:58px;display:flex;gap:4px}
.main-nav a{font-size:11px;font-weight:600;color:#555;text-decoration:none;padding:6px 12px;text-transform:uppercase}
.main-nav a.active{background:var(--red);color:#fff;border-radius:3px}

/* hero */
.hero{left:0;top:88px;width:1200px;height:432px;background:linear-gradient(180deg,#9a9ea3 0%,#6c7076 45%,#3e4146 100%)}
.hero-text{left:0;top:372px;width:1200px;text-align:center;color:#fff;font-size:26px;font-weight:300;line-height:36px;text-transform:uppercase;text-shadow:0 2px 4px rgba(0,0,0,.5)}
.hero-text strong{font-weight:700}
.hero-btn{left:522px;top:446px;width:156px;height:34px;background:var(--red);color:#fff;font-size:12px;font-weight:600;display:flex;align-items:center;justify-content:center;border-radius:3px}
.hero-arrow{top:284px;width:22px;height:44px;background:rgba(0,0,0,.45);color:#fff;display:flex;align-items:center;justify-content:center;font-size:16px}

/* process */
.section-title{width:1200px;left:0;text-align:center;font-size:34px;font-weight:300;color:#555}
.section-title strong{font-weight:700;color:#333}
.section-sub{width:1200px;left:0;text-align:center;font-size:12px;color:var(--muted)}
.process-line{left:250px;top:682px;width:700px;height:2px;background:#cfcfcf}
.step{top:640px;width:280px;text-align:center}
.step-icon{width:84px;height:84px;margin:0 auto;background:var(--light);display:flex;align-items:center;justify-content:center}
.step h3{font-size:18px;font-weight:400;color:#444;margin-top:16px}
.step p{font-size:11px;color:var(--muted);line-height:16px;margin-top:8px;padding:0 30px}

/* screen band */
.screen-band{left:0;top:880px;width:1200px;height:380px;background:linear-gradient(180deg,var(--dark2),var(--dark))}
.screen{left:120px;top:920px;width:960px;height:310px;background:#0c0c0c;border-radius:14px;padding:16px}
.screen-inner{width:100%;height:100%;background:linear-gradient(180deg,var(--blue),var(--blue-dark));position:relative}
.screen-icons{position:absolute;left:0;right:0;top:56px;display:flex;justify-content:center;gap:250px}
.screen-text{position:absolute;left:90px;right:90px;top:186px;color:#dbe9f7;font-size:11px;line-height:17px;text-align:center}

/* clients */
.clients{left:0;top:1260px;width:1200px;height:430px;background:#f3f3f3}
.client{top:1372px;width:208px}
.client-photo{width:208px;height:200px;background:linear-gradient(180deg,#d7d7d7,#9e9e9e);border:4px solid #fff;box-shadow:0 1px 4px rgba(0,0,0,.2);position:relative}
.client-badge{position:absolute;right:-4px;bottom:-4px;width:30px;height:30px;background:var(--blue)}
.client h4{font-size:13px;font-weight:600;margin-top:14px;color:#333}
.client span{display:block;font-size:10px;color:var(--muted);margin-top:2px}
.dots{left:576px;top:1668px;display:flex;gap:8px}
.dots i{width:8px;height:8px;border-radius:50%;background:#bbb}
.dots i.on{background:var(--blue)}

/* info boxes */
.info-box{top:1700px;width:356px;height:228px;background:var(--paper);padding:18px 22px;box-shadow:0 1px 3px rgba(0,0,0,.1)}
.info-box .mark{width:18px;height:18px;background:var(--blue);float:left;margin:6px 10px 0 0}
.info-box h3{font-size:24px;font-weight:300;color:#444}
.info-box h3 strong{font-weight:700}
.info-box p{clear:both;font-size:11px;color:var(--muted);line-height:17px;margin-top:14px}

/* contact */
.contact{left:228px;top:1948px;width:744px;height:252px;background:var(--paper);padding:22px 24px;box-shadow:0 1px 3px rgba(0,0,0,.1)}
.contact h3{font-size:24px;font-weight:300;color:#444}
.contact h3 strong{font-weight:700}
.contact .intro{font-size:10px;color:var(--muted);margin-top:4px}
.field{position:absolute;border:1px solid #ddd;background:#fafafa;font-size:10px;color:#999;padding:6px 8px}
.send-btn{position:absolute;left:24px;top:198px;width:72px;height:26px;background:var(--red);color:#fff;font-size:11px;display:flex;align-items:center;justify-content:center;border-radius:2px}

/* footer */
.site-footer{left:0;top:2236px;width:1200px;height:120px;background:var(--dark)}
.footer-nav{left:236px;top:2286px;display:flex;gap:18px}
.footer-nav a{font-size:10px;color:#999;text-decoration:none;text-transform:uppercase}
.copyright{left:236px;top:2306px;font-size:10px;color:#777}
.social{left:880px;top:2282px;display:flex;gap:10px}
.social i{width:24px;height:24px;border-radius:50%;background:#555}
.social i.hot{background:var(--red)}
</style>
</head>
<body>

<header class="site-header abs">
  <div class="brand abs">The Lumenfold Group</div>
  <div class="contact-tab abs"><span>&#9742; (555) 014-2280</span><span>&#9993; info@lumenfoldgroup.com</span></div>
  <nav class="main-nav abs">
    <a class="active">Home</a><a>Services</a><a>About</a><a>Clients</a><a>Contact Us</a>
  </nav>
</header>

<div class="hero abs" role="img" aria-label="Group of business consultants standing in front of a city skyline"></div>
<div class="hero-arrow abs" style="left:0">&#8249;</div>
<div class="hero-arrow abs" style="left:1178px">&#8250;</div>
<h1 class="hero-text abs">We are a New York/New Jersey based consulting<br>firm with <strong>bold ideas for affecting change</strong></h1>
<div class="hero-btn abs">LEARN MORE &#8250;</div>

<h2 class="section-title abs" style="top:558px">Our unique <strong>Marketing Process</strong></h2>
<p class="section-sub abs" style="top:606px">And we make them</p>
<div class="process-line abs"></div>

<div class="step abs" style="left:170px">
  <div class="step-icon"><svg width="44" height="40" viewBox="0 0 44 40"><rect x="2" y="10" width="40" height="28" rx="3" fill="var(--blue)"/><rect x="15" y="3" width="14" height="9" rx="2" fill="none" stroke="var(--blue)" stroke-width="3"/><rect x="2" y="20" width="40" height="3" fill="#fff"/></svg></div>
  <h3>Researching</h3>
  <p>We study each market closely, gather the facts that matter and map the ground before any plan is set.</p>
</div>
<div class="step abs" style="left:460px">
  <div class="step-icon"><svg width="44" height="44" viewBox="0 0 44 44"><circle cx="22" cy="22" r="19" fill="none" stroke="var(--blue)" stroke-width="3"/><ellipse cx="22" cy="22" rx="8" ry="19" fill="none" stroke="var(--blue)" stroke-width="3"/><line x1="3" y1="22" x2="41" y2="22" stroke="var(--blue)" stroke-width="3"/></svg></div>
  <h3>Networking</h3>
  <p>We connect leaders, partners and communities so that good ideas find the people who can move them.</p>
</div>
<div class="step abs" style="left:750px">
  <div class="step-icon"><svg width="48" height="42" viewBox="0 0 48 42"><path d="M2 4h8l6 24h24l5-16H13" fill="none" stroke="var(--blue)" stroke-width="3.5" stroke-linejoin="round"/><circle cx="19" cy="36" r="3.5" fill="var(--blue)"/><circle cx="37" cy="36" r="3.5" fill="var(--blue)"/></svg></div>
  <h3>Developing</h3>
  <p>We turn insight into action with clear strategies that grow stronger companies and smarter leaders.</p>
</div>

<div class="screen-band abs"></div>
<div class="screen abs">
  <div class="screen-inner">
    <div class="screen-icons">
      <svg width="64" height="58" viewBox="0 0 44 40"><rect x="2" y="10" width="40" height="28" rx="3" fill="#fff"/><rect x="15" y="3" width="14" height="9" rx="2" fill="none" stroke="#fff" stroke-width="3"/><rect x="2" y="20" width="40" height="3" fill="var(--blue)"/></svg>
      <svg width="60" height="60" viewBox="0 0 44 44"><circle cx="22" cy="22" r="19" fill="none" stroke="#fff" stroke-width="3"/><ellipse cx="22" cy="22" rx="8" ry="19" fill="none" stroke="#fff" stroke-width="3"/><line x1="3" y1="22" x2="41" y2="22" stroke="#fff" stroke-width="3"/></svg>
      <svg width="66" height="58" viewBox="0 0 48 42"><path d="M2 4h8l6 24h24l5-16H13" fill="none" stroke="#fff" stroke-width="3.5" stroke-linejoin="round"/><circle cx="19" cy="36" r="3.5" fill="#fff"/><circle cx="37" cy="36" r="3.5" fill="#fff"/></svg>
    </div>
    <p class="screen-text">We develop innovative strategies for marketing, strategic planning, business development, public relations and economic development. Simply put, we create innovative strategies for invigorating smarter and stronger leaders and companies. We are a consulting firm with bold ideas for affecting change.</p>
  </div>
</div>

<div class="clients abs"></div>
<h2 class="section-title abs" style="top:1292px;font-size:30px">A very <strong>Renowned Client</strong> we have</h2>
<p class="section-sub abs" style="top:1336px">We're proud of our partners</p>

<div class="client abs" style="left:148px"><div class="client-photo" role="img" aria-label="Portrait of client Nora Quill"><div class="client-badge"></div></div><h4>Nora Quill</h4><span>Managing Director, Northline</span></div>
<div class="client abs" style="left:380px"><div class="client-photo" role="img" aria-label="Portrait of client Felix Arden"><div class="client-badge"></div></div><h4>Felix Arden</h4><span>CEO, Harbor Works</span></div>
<div class="client abs" style="left:612px"><div class="client-photo" role="img" aria-label="Portrait of client Mara Solberg"><div class="client-badge"></div></div><h4>Mara Solberg</h4><span>Founder, Civic Growth Fund</span></div>
<div class="client abs" style="left:844px"><div class="client-photo" role="img" aria-label="Portrait of client Owen Tarrow"><div class="client-badge"></div></div><h4>Owen Tarrow</h4><span>Director, Regional Partners</span></div>
<div class="dots abs"><i></i><i class="on"></i><i></i><i></i></div>

<div class="info-box abs" style="left:228px">
  <span class="mark"></span><h3>About <strong>our company</strong></h3>
  <p>The Lumenfold Group is a consulting firm based in New York and New Jersey. We help private companies, development groups and public bodies plan for growth, build strong partnerships and invest in their communities with confidence and a clear view ahead.</p>
</div>
<div class="info-box abs" style="left:616px">
  <span class="mark"></span><h3><strong>Services</strong> we provide</h3>
  <p>Marketing strategy, strategic planning, business development and public relations for economic development. Each plan is shaped around your goals, measured with care and built to deliver change that lasts well beyond the first step of the work.</p>
</div>

<section class="contact abs">
  <h3><strong>Contact</strong> us</h3>
  <p class="intro">Fill out the form below and we will be in touch with you soon.</p>
  <div class="field" style="left:24px;top:92px;width:236px;height:26px">Name</div>
  <div class="field" style="left:24px;top:136px;width:236px;height:26px">Email</div>
  <div class="field" style="left:276px;top:92px;width:236px;height:70px">Notes</div>
  <div class="send-btn">Send</div>
</section>

<footer class="site-footer abs"></footer>
<nav class="footer-nav abs"><a>Home</a><a>Services</a><a>About</a><a>Clients</a><a>Contact Us</a></nav>
<p class="copyright abs">&copy; The Lumenfold Group &middot; info@lumenfoldgroup.com</p>
<div class="social abs"><i></i><i class="hot"></i><i></i></div>

</body>
</html>
```